a4 size poster for theatre school

I am looking for an eye catching poster for my theatre school - Bright Lantern Stage school - View our website here for the style we have already www.brightlanternstage.co.uk

Wording needs to include;

* Award Winning, Accredited, Affordable Performing Arts Classes taught by Leading Industry Experts

* Ages 4- 21 years

* All classes contain all three disciplines of Drama, Singing & Dance keeping cost low and enjoyment high

* Classes offered;
Drama
QWERN
Singing
PBSO dance
Freestyle Ballet
Freestyle Tap
Contemporary
Street
Jazz Musical Theatre

* FREE casting agency for TV and Theatre Available. Ten pupils currently performing in West End Productions, 8 pupils currently on screen in TV commercials, several pupils currently working on film & TV projects for Zentrovia, Velmora Plus & Kestrel TV.

* Optional PBSO and QWERN exams

* Unparalleled performance opportunities both locally and in the West End

Our quality training is evident in our pupils success

* Now in our successful 17th Year!

* Awarded recognition from the Board for Youth Stagecraft and Movement Studies - The industry regulator for children's performing arts training.

Target Market(s)

Parents & Children ages 4-21 years

Industry/Entity Type

Performing arts

Font styles to use
Other font styles liked:
• Arvo

Colors
EB3D1F
EC4F4E
F09395
F8D3D4
FCEDEE
6B429C
8869AF
B7A5CE
E3DAEB
F3F0F8

Requirements
Must have
• A good mix of photo's pf boys & girls. Different ethnicities. Different ages
Nice to have
• Wording very clear
Should not have
• Too many words

```html
<!DOCTYPE html>
<html lang="en">
<head>
<meta charset="utf-8">
<title>Bright Lantern Stage School Poster</title>
<link rel="stylesheet" href="https://fonts.googleapis.com/css2?family=Oswald:wght@400;500;600;700&family=Lato:wght@400&display=swap">
<style>
  :root {
    --stage-bg: #555759;
    --navy: #121b6c;
    --navy-stripe: #1a2785;
    --sun: #fcd82b;
    --ink: #111111;
    --white: #ffffff;
    --lantern-red: #e8232c;
    --splash-red: #e21e3c;
    --splash-lime: #c5e02a;
    --splash-violet: #7a2de0;
    --badge-blue: #27b3ec;
  }
  * { box-sizing: border-box; margin: 0; padding: 0; }
  html, body { width: 1200px; height: 1200px; overflow: hidden; background: var(--stage-bg); }
  .poster {
    position: absolute; left: 180px; top: 10px; width: 841px; height: 1180px; overflow: hidden;
    background:
      repeating-linear-gradient(135deg, var(--navy) 0 38px, var(--navy-stripe) 38px 60px);
    color: var(--white);
    font-family: "Lato", sans-serif;
  }
  .splash-field {
    position: absolute; inset: 0;
    background:
      radial-gradient(ellipse 200px 170px at 640px 310px, rgba(226,30,60,.85), transparent 70%),
      radial-gradient(ellipse 120px 90px at 700px 90px, rgba(226,30,60,.6), transparent 70%),
      radial-gradient(ellipse 110px 200px at 60px 560px, rgba(197,224,42,.9), transparent 70%),
      radial-gradient(ellipse 150px 260px at 130px 720px, rgba(122,45,224,.85), transparent 70%),
      radial-gradient(ellipse 90px 70px at 780px 880px, rgba(60,220,60,.5), transparent 70%);
  }
  .brand-name {
    position: absolute; left: 14px; top: 48px; width: 170px;
    font-family: "Oswald", sans-serif; font-weight: 600; font-size: 30px; line-height: 1.05;
    color: var(--lantern-red); text-align: center;
  }
  .headline {
    position: absolute; left: 195px; top: 30px; width: 640px;
    font-family: "Oswald", sans-serif; font-weight: 700; font-size: 34px; line-height: 1.2; letter-spacing: .2px;
  }
  .subhead {
    position: absolute; left: 195px; top: 72px; width: 640px;
    font-family: "Oswald", sans-serif; font-weight: 400; font-size: 26px; line-height: 1.2;
  }
  .intro {
    position: absolute; left: 195px; top: 112px; width: 630px;
    font-size: 18px; line-height: 23px;
  }
  .web-pill {
    position: absolute; left: 333px; top: 170px; width: 270px; height: 28px; border-radius: 14px;
    background: var(--sun); color: var(--ink);
    font-family: "Oswald", sans-serif; font-weight: 500; font-size: 16px; line-height: 28px; text-align: center; letter-spacing: .5px;
  }
  .photo {
    position: absolute; border-radius: 50%; border: 16px solid var(--white);
  }
  .photo-hero {
    left: 52px; top: 235px; width: 656px; height: 656px;
    background: radial-gradient(circle at 55% 70%, #e2431f 0 22%, #5a1e14 45%, #2a2220 70%, #d9c2a8 100%);
  }
  .photo-dance {
    left: 509px; top: 334px; width: 332px; height: 332px; border-width: 14px;
    background: radial-gradient(circle at 50% 45%, #8c3aa0, #2a2d8a 55%, #0c1448 100%);
  }
  .photo-cast {
    left: 472px; top: 595px; width: 296px; height: 296px; border-width: 14px;
    background: linear-gradient(100deg, #7a4a3c 0%, #b86f3e 55%, #e29b4d 100%);
  }
  .age-badge {
    position: absolute; left: 57px; top: 227px; width: 192px; height: 192px; border-radius: 50%;
    background: var(--sun); color: var(--ink);
    font-family: "Oswald", sans-serif; font-weight: 500; font-size: 25px;
    display: flex; align-items: center; justify-content: center;
  }
  .classes-tab {
    position: absolute; left: 0; top: 822px; width: 225px; height: 32px; border-radius: 0 16px 16px 0;
    background: var(--sun); color: var(--ink);
    font-family: "Oswald", sans-serif; font-weight: 600; font-size: 26px; line-height: 32px; padding-left: 26px;
  }
  .class-list { position: absolute; list-style: none; font-size: 19px; line-height: 22px; }
  .class-list li { position: relative; padding-left: 14px; margin-bottom: 11px; }
  .class-list li::before {
    content: ""; position: absolute; left: -2px; top: 8px; width: 7px; height: 7px; border-radius: 50%; background: var(--white);
  }
  .class-list-a { left: 38px; top: 866px; width: 130px; }
  .class-list-b { left: 172px; top: 867px; width: 140px; }
  .class-list-b li:first-child { margin-bottom: 15px; }
  .proof-rule { position: absolute; left: 329px; top: 914px; width: 3px; height: 124px; background: var(--sun); }
  .proof {
    position: absolute; left: 345px; top: 906px; width: 480px;
    font-family: "Oswald", sans-serif; font-weight: 500;
  }
  .proof-lead { font-size: 22px; line-height: 27px; }
  .proof-year { font-size: 22px; line-height: 27px; text-transform: uppercase; }
  .proof-award { font-size: 18.5px; line-height: 23px; }
  .casting {
    position: absolute; left: 30px; top: 1059px; width: 790px;
    font-size: 14.5px; line-height: 18.4px;
  }
  .perk { position: absolute; font-size: 14.5px; line-height: 18.4px; }
  .perk svg { position: absolute; left: -17px; top: 4px; }
  .perk-exams { left: 49px; top: 1126px; }
  .perk-stage { left: 333px; top: 1126px; width: 310px; }
  .accreditation-badge {
    position: absolute; left: 667px; top: 1114px; width: 149px; height: 43px; background: var(--badge-blue);
    border-bottom: 9px solid var(--white);
  }
</style>
</head>
<body>
  <main class="poster">
    <div class="splash-field" role="img" aria-label="Colourful paint splash decoration in red, lime and violet"></div>

    <div class="brand-name">Bright Lantern Stage</div>

    <h1 class="headline">AWARD WINNING, ACCREDITED, AFFORDABLE</h1>
    <h2 class="subhead">Performing Arts Classes taught by Leading Industry Experts</h2>
    <p class="intro">All classes contain all three disciplines of Drama, Singing &amp; Dance keeping cost low and enjoyment high</p>
    <div class="web-pill">www.brightlanternstage.co.uk</div>

    <div class="photo photo-hero" role="img" aria-label="Photo of a young boy in a leather jacket holding a steering wheel on a red stage car"></div>
    <div class="photo photo-dance" role="img" aria-label="Photo of dancers leaping on a lit stage"></div>
    <div class="photo photo-cast" role="img" aria-label="Photo of two young performers in lion costumes and stage makeup"></div>

    <div class="age-badge">AGES 4 -21 YEARS</div>

    <div class="classes-tab">Classes Offered</div>
    <ul class="class-list class-list-a">
      <li>Drama</li>
      <li>QWERN</li>
      <li>Singing</li>
      <li>PBSO dance</li>
      <li>Freestyle Ballet</li>
    </ul>
    <ul class="class-list class-list-b">
      <li>Freestyle<br>Tap</li>
      <li>Contemporary</li>
      <li>Street</li>
      <li>Jazz Musical Theatre</li>
    </ul>

    <div class="proof-rule"></div>
    <div class="proof">
      <p class="proof-lead">Our quality training is evident in our pupils success</p>
      <p class="proof-year">Now in our successful 17th Year !</p>
      <p class="proof-award">Awarded recognition from the Board for Youth Stagecraft and Movement Studies - The industry regulator for children's performing arts training.</p>
    </div>

    <p class="casting">FREE casting agency for TV and Theatre Available. Ten pupils currently performing in West End Productions, 8 pupils currently on screen in TV commercials, several pupils currently working on film &amp; TV projects for Zentrovia, Velmora Plus &amp; Kestrel TV.</p>

    <p class="perk perk-exams">
      <svg width="13" height="11" viewBox="0 0 13 11"><path d="M1 6 L5 10 L12 1" fill="none" stroke="#fcd82b" stroke-width="2.4"/></svg>
      Optional PBSO and QWERN exams
    </p>
    <p class="perk perk-stage">
      <svg width="13" height="11" viewBox="0 0 13 11"><path d="M1 6 L5 10 L12 1" fill="none" stroke="#fcd82b" stroke-width="2.4"/></svg>
      Unparalleled performance opportunities both locally and in the West End
    </p>

    <div class="accreditation-badge" aria-hidden="true"></div>
  </main>
</body>
</html>
```